Mouse and Rodent Infestation Spray

Need to Design label for 16oz bottle. The image sent has our initial design on it. Need other options.

Industry/Entity Type

Pest Control

Colors

Designer to choose colors to be used in the design.

```html
<!DOCTYPE html>
<html lang="en">
<head>
<meta charset="utf-8">
<title>Pestara Mouse &amp; Rat Infestation Label</title>
<link rel="stylesheet" href="https://fonts.googleapis.com/css2?family=Anton&family=Oswald:wght@500;600;700&display=swap">
<style>
  :root {
    --page: #ffffff;
    --label-white: #f7f8f8;
    --blue-deep: #2a5ea8;
    --blue-mid: #3d7fc6;
    --blue-light: #8cc6ec;
    --green: #3aa83c;
    --green-bright: #5cc84a;
    --green-dark: #1f7a2a;
    --title-light: #eef0f2;
    --title-shadow: rgba(20, 30, 40, .55);
    --ink: #1f2a2e;
    --ink-soft: #ffffff;
    --prohibit: #c8252c;
    --seal-dark: #1d5d28;
    --seal-mid: #2f8a3c;
  }
  * { box-sizing: border-box; margin: 0; padding: 0; }
  html, body { width: 1200px; height: 1200px; overflow: hidden; background: var(--page); }
  .canvas { position: relative; width: 1200px; height: 1200px; }
  .label {
    position: absolute; left: 50px; top: 185px; width: 1100px; height: 830px;
    background: var(--label-white); overflow: hidden;
    font-family: "Oswald", "Arial Narrow", sans-serif;
  }
  .label__band {
    position: absolute; left: 0; top: 0; width: 100%; height: 330px;
    background: linear-gradient(90deg, var(--blue-deep) 0%, var(--blue-mid) 55%, var(--blue-light) 100%);
  }
  .brand-tag {
    position: absolute; left: 410px; top: 30px; width: 280px; height: 56px;
    background: var(--green); transform: skewX(-18deg);
    display: flex; align-items: center; justify-content: center;
  }
  .brand-tag__name {
    transform: skewX(18deg); color: var(--ink-soft); font-weight: 700;
    font-size: 38px; line-height: 1; letter-spacing: 1px;
  }
  .title {
    position: absolute; left: 0; width: 100%; top: 98px; text-align: center;
    font-family: "Anton", "Impact", sans-serif; font-weight: 400; color: var(--title-light);
    font-size: 108px; line-height: 110px; letter-spacing: 1px;
    text-shadow: 3px 4px 0 var(--title-shadow);
  }
  .title__line { display: block; }
  .ribbon {
    position: absolute; left: 300px; top: 346px; width: 500px; height: 54px;
    background: var(--green-bright); clip-path: polygon(4% 0, 100% 0, 96% 100%, 0 100%);
    display: flex; align-items: center; justify-content: center;
    color: var(--ink-soft); font-weight: 500; font-size: 30px;
  }
  .benefits { position: absolute; left: 240px; top: 432px; list-style: none; }
  .benefits__item {
    display: flex; align-items: center; gap: 6px; height: 42px;
    font-weight: 700; font-size: 34px; color: var(--ink);
  }
  .benefits__item:nth-child(2) { margin-left: 22px; }
  .benefits__tick { width: 44px; height: 40px; }
  .meadow {
    position: absolute; left: 0; top: 575px; width: 100%; height: 255px;
    background: linear-gradient(180deg, var(--green-bright) 0%, var(--green) 45%, var(--green-dark) 100%);
    clip-path: polygon(0 12%, 8% 4%, 20% 10%, 34% 2%, 50% 8%, 66% 0, 80% 7%, 92% 2%, 100% 8%, 100% 100%, 0 100%);
  }
  .mouse-visual {
    position: absolute; left: 660px; top: 425px; width: 220px; height: 220px;
    border-radius: 50%; background: radial-gradient(circle, #d6b48f 0%, #b89270 55%, #f1e6da 100%);
  }
  .mouse-visual__ring { position: absolute; inset: 0; }
  .ingredients {
    position: absolute; left: 240px; top: 672px; color: var(--ink-soft);
    font-weight: 500; font-size: 28px; line-height: 34px;
  }
  .seal { position: absolute; }
  .seal--natural { left: 585px; top: 680px; width: 72px; height: 72px; border-radius: 50%; background: var(--seal-dark); }
  .seal--formula { left: 690px; top: 692px; width: 110px; height: 48px; background: var(--blue-mid); clip-path: polygon(12% 0, 100% 0, 88% 100%, 0 100%); }
  .seal--safety { left: 830px; top: 676px; width: 76px; height: 76px; border-radius: 50%; background: var(--seal-mid); }
</style>
</head>
<body>
<div class="canvas">
  <section class="label">
    <div class="label__band"></div>
    <div class="brand-tag"><span class="brand-tag__name">PESTARA</span></div>
    <h1 class="title">
      <span class="title__line">MOUSE &amp; RAT</span>
      <span class="title__line">INFESTATION</span>
    </h1>
    <div class="ribbon">SAFE FOR INDOR OUTDOOR USE</div>
    <div class="meadow" role="img" aria-label="Illustrated green grass along the bottom of the label"></div>
    <ul class="benefits">
      <li class="benefits__item"><svg class="benefits__tick" viewBox="0 0 44 40"><path d="M4 22 L16 34 L40 4" fill="none" stroke="#3aa83c" stroke-width="7" stroke-linecap="round" stroke-linejoin="round"/></svg>NATURAL BAIT</li>
      <li class="benefits__item"><svg class="benefits__tick" viewBox="0 0 44 40"><path d="M4 22 L16 34 L40 4" fill="none" stroke="#3aa83c" stroke-width="7" stroke-linecap="round" stroke-linejoin="round"/></svg>FREE OF PESTICIDES</li>
      <li class="benefits__item"><svg class="benefits__tick" viewBox="0 0 44 40"><path d="M4 22 L16 34 L40 4" fill="none" stroke="#3aa83c" stroke-width="7" stroke-linecap="round" stroke-linejoin="round"/></svg>LONG LASTING CONTROL</li>
    </ul>
    <div class="mouse-visual" role="img" aria-label="Photo of a mouse inside a red prohibition sign">
      <svg class="mouse-visual__ring" viewBox="0 0 220 220"><circle cx="110" cy="110" r="99" fill="none" stroke="#c8252c" stroke-width="17"/><line x1="40" y1="40" x2="180" y2="180" stroke="#c8252c" stroke-width="17"/></svg>
    </div>
    <p class="ingredients">ACTIVE INGREDIENTS:<br>48% PEPPERMINT OIL<br>52% SMART INGREDIENTS</p>
    <div class="seal seal--natural"></div>
    <div class="seal seal--formula"></div>
    <div class="seal seal--safety"></div>
  </section>
</div>
</body>
</html>
```